financial company web page

We are tax and financial consulting company that needs a web site. Our logo is attached. Headquarters of our company is based in Latvia, Riga. Our actual temporary web site is www.norquill.com The main purpose of our new web site is:
* to explain the benefits of doing business through Latvian LLC companies;
* provide necessary information about taxation regime in Latvia for trading and holding companies
* propose some standard schemes of using Latvian companies for various businesses.
* offer our clients other jurisdictions companies - other European, offshore, etc.
* offer our clients ecommerce solutions
* offer our client residency in Latvia and EU
Registration of a Latvian company + accounting + legal advice will be our primary product. However, web site first page should highlight 4 other important products, such as:
1 - eCommerce (here we will explain briefly what is eCommerce, how our client can use it, what are the bonuses doing business online, explain conditions of eCommerce, etc) ;
2 - Residence Permit (here we offer EU and non-EU citizens to obtain Latvian residence permit and explain the benefits of having Latvian ID card);
3 - other Jurisdictions (here we propose list of other companies registered in the countries with favorable taxation regime, i.e. UK, Hong-Kong, Canada, Panama, BVI, UAE, etc);
4 - banking (here we explain benefits of having bank account in Latvia, explaining briefly products that bank offer, etc).
Overall Website map is the following:
1. About us
2. About Latvia
3. Contacts
4. Latvian company
5. Our services
a. еCommerce
b. Resident permit (Latvia and EU)
c. Bank accounts
d. Registration and support of other jurisdictions (European companies, Low tax companies, Offshore companies)
e. Additional services (Tax advisory, Virtual office, European licenses, Accounting services, Legal address in Riga)
6. Become Partner
7. Tembrole Travel Guide
As a start point we need only first page design. If this design suits us well we will continue to work with you on other pages. We are looking for innovative, creative and professional design in line with our corporate logo and colours. We want this design to focus more on graphic, on simplicity and usability. It should be immediately clear from the first glance what the site is about, what is our key product and how to get more information if I'm interested on something.
These are website from our sector, we want to be better:
http://www.vantel-ridge.com/
http://www.qpr-harbourline.com/
http://www.dxlventurebuilders.com/
http://www.firmstarter318.co.uk/
In case you can't find our logo, please, ask I will send it to your mail. Thanks!
Target Market(s)
European, Russian or Chinesee enterpreneurs
Industry/Entity Type
Accounting
Requirements
Must have
- Web site will be on 10 languages, so somewhere must be a button/flag to switch language.
Contact information should be on every page (phone number and add Skype buttons or similar).
Search button should be available on the first page
Button Request a Call should be on every page.
Visitors should also have a possibility to download a brochure about each product (so appropriate button should be in each section).

```html
<!DOCTYPE html>
<html lang="en">
<head>
<meta charset="utf-8">
<title>Tembrole – Tax and Financial Solutions</title>
<link href="https://fonts.googleapis.com/css2?family=Ubuntu:wght@400;500&family=Roboto:wght@300;400&display=swap" rel="stylesheet">
<style>
:root{
  --navy:#233a7a;
  --navy-dark:#1f3270;
  --red:#b3303d;
  --ink:#333;
  --muted:#555;
  --panel:#f3f2f3;
}
*{margin:0;padding:0;box-sizing:border-box}
html,body{width:900px;height:1200px;overflow:hidden;background:#fff}
body{position:relative;font-family:'Roboto',sans-serif;color:var(--ink)}
.abs{position:absolute}

/* header */
.brand{left:38px;top:26px;display:flex;align-items:center;gap:10px}
.brand-dot{width:30px;height:30px;border-radius:50%;background:var(--navy)}
.brand-name{font-family:'Ubuntu',sans-serif;font-weight:500;font-size:36px;color:var(--navy)}
.contact{left:410px;font-family:'Ubuntu',sans-serif;font-size:16px;color:#333;display:flex;align-items:center;gap:8px}
.lang{left:711px;top:10px;width:151px;height:22px;border:1px solid #999;background:#fff;font-family:'Ubuntu',sans-serif;font-size:14px;padding:2px 6px;display:flex;align-items:center;gap:6px}
.lang .caret{margin-left:auto}
.search{left:693px;top:58px;width:175px;height:24px;border:1px solid #bbb;background:#fff;font-size:15px;color:#bbb;padding:3px 7px;font-family:'Ubuntu',sans-serif}
.search-btn{left:829px;top:58px;width:39px;height:24px;background:#a8a8a8;display:flex;align-items:center;justify-content:center}

/* nav */
.nav{left:0;top:93px;width:900px;height:39px;background:var(--navy);border-bottom:3px solid var(--red)}
.nav-home{left:26px;top:89px;width:53px;height:43px;background:var(--red);border-radius:4px 4px 0 0}
.nav-item{top:103px;font-family:'Ubuntu',sans-serif;font-size:14px;color:#fff;white-space:nowrap}

/* hero */
.hero{left:0;top:135px;width:900px;height:362px;background:linear-gradient(180deg,#9fb2c8 0%,#c9d3dd 30%,#d9dde2 50%,#8b7466 75%,#5b4c46 100%)}
.hero-panel{left:26px;top:298px;width:454px;height:188px;background:rgba(255,255,255,.82);border-radius:8px}
.hero-title{left:45px;top:312px;font-family:'Ubuntu',sans-serif;font-size:40px;font-weight:500;color:var(--red)}
.hero-sub{left:45px;top:358px;font-family:'Ubuntu',sans-serif;font-size:17px;line-height:22px;white-space:nowrap}
.hero-sub .accent{color:var(--red)}
.hero-btn{left:43px;top:419px;width:165px;height:35px;background:linear-gradient(#666,#444);border-radius:3px;color:#fff;font-family:'Ubuntu',sans-serif;font-size:16px;line-height:35px;text-align:center;box-shadow:0 2px 3px rgba(0,0,0,.3)}
.hero-person{left:352px;top:312px;width:125px;height:174px;background:linear-gradient(#d6d6d6,#2b2b2b);border-radius:50px 50px 6px 6px}

/* product cards */
.card{top:517px;width:186px}
.card-img{width:180px;height:134px;border:2px solid #999}
.card-title{font-family:'Ubuntu',sans-serif;font-size:20px;color:var(--navy);margin-top:18px}
.card-text{font-size:11.5px;line-height:16.5px;color:var(--muted);margin-top:5px}
.card-more{position:absolute;top:243px;right:10px;font-family:'Ubuntu',sans-serif;font-size:13px;color:var(--navy)}
.card-bar{position:absolute;top:264px;left:-3px;width:180px;height:4px;background:var(--navy)}
.card-bar.red{background:var(--red)}

/* lower sections */
.section-title{font-family:'Ubuntu',sans-serif;font-size:20px;color:var(--navy);font-weight:400}
.about-text{left:26px;top:850px;width:387px;font-size:11.5px;line-height:16.2px;color:#444;text-align:justify}
.about-text p+p{margin-top:16px}
.services-box{left:437px;top:854px;width:425px;height:203px;background:var(--panel)}
.service-list{list-style:none;font-size:12.5px;color:#444;position:absolute}
.service-list li{height:27px;display:flex;align-items:center;gap:11px}
.service-list li::before{content:"";border-left:6px solid var(--red);border-top:4px solid transparent;border-bottom:4px solid transparent}

/* footer */
.footer{left:0;top:1080px;width:900px;height:120px;background:var(--navy-dark);border-top:3px solid var(--red);color:#fff;text-align:center;font-family:'Ubuntu',sans-serif}
.footer-links{margin-top:28px;font-size:12.5px;font-weight:500}
.footer-links span{margin:0 5px}
.footer-line{font-size:12px;font-weight:500;margin-top:3px}
.footer-copy{font-size:10px;margin-top:5px}
</style>
</head>
<body>

<header>
  <div class="abs brand"><span class="brand-dot"></span><span class="brand-name">Tembrole</span></div>
  <div class="abs contact" style="top:29px">
    <svg width="20" height="20" viewBox="0 0 20 20"><path d="M5 2c-2 1-3 3-2 6 2 5 5 8 9 10 3 1 5 0 6-2l-3-3-2 2c-3-1-5-4-6-6l2-2z" fill="none" stroke="#999" stroke-width="1.4"/></svg>
    <span>+ 371 2045619</span>
  </div>
  <div class="abs contact" style="top:56px">
    <svg width="20" height="16" viewBox="0 0 20 16"><rect x="1" y="1" width="18" height="14" fill="none" stroke="#999" stroke-width="1.4"/><path d="M4 6h6M4 10h4" stroke="#999"/></svg>
    <span>info@tembrole.com</span>
  </div>
  <div class="abs lang">English
    <svg width="30" height="16" viewBox="0 0 30 16"><rect width="30" height="16" fill="#25408f"/><path d="M0 0L30 16M30 0L0 16" stroke="#fff" stroke-width="3"/><path d="M15 0v16M0 8h30" stroke="#fff" stroke-width="5"/><path d="M15 0v16M0 8h30" stroke="#c8102e" stroke-width="3"/></svg>
    <svg class="caret" width="12" height="10" viewBox="0 0 12 10"><path d="M0 0h12L6 10z" fill="#233a7a"/></svg>
  </div>
  <div class="abs search">Search</div>
  <div class="abs search-btn"><svg width="18" height="18" viewBox="0 0 18 18"><circle cx="7" cy="7" r="5" fill="none" stroke="#222" stroke-width="2"/><path d="M11 11l6 6" stroke="#222" stroke-width="3"/></svg></div>
</header>

<nav>
  <div class="abs nav"></div>
  <div class="abs nav-home"></div>
  <span class="abs nav-item" style="left:37px">Home</span>
  <span class="abs nav-item" style="left:102px">About us</span>
  <span class="abs nav-item" style="left:186px">About Latvia</span>
  <span class="abs nav-item" style="left:292px">Contacts</span>
  <span class="abs nav-item" style="left:377px">Latvian company</span>
  <span class="abs nav-item" style="left:511px">Our services</span>
  <span class="abs nav-item" style="left:617px">Become Partner</span>
  <span class="abs nav-item" style="left:743px">Tembrole Travel Guide</span>
</nav>

<section>
  <div class="abs hero" role="img" aria-label="Winter panorama of Riga old town with cathedral tower and river bridge"></div>
  <div class="abs hero-panel"></div>
  <div class="abs hero-title">Latvia</div>
  <div class="abs hero-sub">Your platform for<br><span class="accent">International business and Capital</span></div>
  <div class="abs hero-btn">View our services</div>
  <div class="abs hero-person" role="img" aria-label="Smiling business consultant in a suit with arms crossed"></div>
</section>

<section>
  <div class="abs card" style="left:42px">
    <div class="card-img" role="img" aria-label="Businesswoman with laptop giving a thumbs up" style="background:linear-gradient(135deg,#c9d4de,#7a6a62)"></div>
    <div class="card-title">E-commerce</div>
    <div class="card-text">Cumaser kertyase socisera natoqu eagnis dist mte dulmuese feugiata sit amm easer ermen .</div>
    <div class="card-more">Read more ››</div>
    <div class="card-bar red"></div>
  </div>
  <div class="abs card" style="left:253px">
    <div class="card-img" role="img" aria-label="Wooden stamp on a Latvian flag document" style="background:linear-gradient(160deg,#f4f1ee,#c55a2a 60%,#a0303a)"></div>
    <div class="card-title">Residence Permit</div>
    <div class="card-text">Cumaser kertyase socisera natoqu eagnis dist mte dulmuese feugiata sit amm easer ermen .</div>
    <div class="card-more">Read more ››</div>
    <div class="card-bar"></div>
  </div>
  <div class="abs card" style="left:467px">
    <div class="card-img" role="img" aria-label="Golden key lying on a page about investing" style="background:linear-gradient(150deg,#eeeeee,#b8b8b8)"></div>
    <div class="card-title">Juridiction</div>
    <div class="card-text">Cumaser kertyase socisera natoqu eagnis dist mte dulmuese feugiata sit amm easer ermen .</div>
    <div class="card-more">Read more ››</div>
    <div class="card-bar"></div>
  </div>
  <div class="abs card" style="left:679px">
    <div class="card-img" role="img" aria-label="Pencil resting on a bank account agreement" style="background:linear-gradient(160deg,#f08a3a 0%,#f7f7f7 30%,#dcdcdc)"></div>
    <div class="card-title">Banking</div>
    <div class="card-text">Cumaser kertyase socisera natoqu eagnis dist mte dulmuese feugiata sit amm easer ermen .</div>
    <div class="card-more">Read more ››</div>
    <div class="card-bar"></div>
  </div>
</section>

<section>
  <h2 class="abs section-title" style="left:29px;top:820px">About Company</h2>
  <div class="abs about-text">
    <p><strong style="color:#222;font-weight:400">Tembrole</strong> is a tax advisory firm established back in 2002 in Limassol, Cyprus. For more than 10 years we are providing tax advisory and company formation services for businesses willing to open new markets, optimize their financial operations and secure private assets.</p>
    <p>We moved our main office to Riga, Latvia in the end of 2011 with the purpose to exploit new opportunities from the fast growing European financial center, as well as to support our existing clients who has already appreciated benefits of using Latvian companies or Bank accounts. We entered into partnership with main Latvian non-residents banks, such as Nordvale, Ostrava Bank, Kestrel, as well as built our own team of professional lawyers, accountants and tax consultants in order to deliver superior service with competitive prices.</p>
  </div>

  <h2 class="abs section-title" style="left:439px;top:820px">Additional Services</h2>
  <div class="abs services-box">
    <ul class="service-list" style="left:20px;top:18px">
      <li>Legal Address in Riga</li>
      <li>Virtual Office Services</li>
      <li>Tax Advisory</li>
      <li>Professional Accounting Services</li>
      <li>Bank Account in Latvia</li>
      <li>VAT Registration</li>
    </ul>
    <ul class="service-list" style="left:242px;top:23px">
      <li>Legal Advisory</li>
      <li>European Licsences</li>
      <li>Latvian Company Website</li>
      <li>Latvian Domain Name</li>
      <li>Car registration in Latvia</li>
    </ul>
  </div>
</section>

<footer class="abs footer">
  <div class="footer-links">Home<span>|</span>About us<span>|</span>About Latvia<span>|</span>Contacts<span>|</span>Latvian company<span>|</span>Our services<span>|</span>Become Partner<span>|</span>Tembrole Travel Guide</div>
  <div class="footer-line" style="margin-top:6px">Kalnu street 12-4, Riga, LV-1050, Latvia</div>
  <div class="footer-line">Phone number: + 371 20456190 &nbsp;|&nbsp; Email:info@tembrole.com</div>
  <div class="footer-copy">Copyright 2013 Tembrole. all rights reserved.</div>
</footer>

</body>
</html>
```